Kelvo App - Live Events Stream

Need mobile first appliation designs for a new location based events and offers application <br/><br/>Will require at least 5 screens creating, namely:<br/><br/>- Landing screen<br/>- Event/Offer listings screen<br/>- Overview of Event/Offer screen<br/>- Chat/Stream for Event/Offer<br/>- Directions for Event/Offer<br/>- Create Event/Offer screen(s)<br/><br/>Will require the design to have a vantor material feel. <br/><br/>See Attached files for further details

Requirements
Must have
• See Doc
Nice to have
• See Doc
Should not have
• See Doc

```html
<!DOCTYPE html>
<html lang="en">
<head>
<meta charset="utf-8">
<title>Kelvo App – Screen Flow</title>
<link rel="stylesheet" href="https://fonts.googleapis.com/css2?family=Roboto:wght@300;400;500;700&display=swap">
<style>
:root{
  --board:#ececec;
  --title:#6f6f6f;
  --screen:#f5f7f9;
  --white:#ffffff;
  --teal:#86d4de;
  --teal-dark:#5cc0cf;
  --pink:#e3a6e0;
  --yellow:#ecd85c;
  --ink:#2f2f33;
  --muted:#8d8f95;
  --line:#e3e6ea;
  --wire:#3a3a3a;
  --photo-a:#1d1638;
  --photo-b:#5b3a97;
  --photo-c:#a070d6;
  --map:#e4e6e8;
}
*{box-sizing:border-box;margin:0;padding:0}
html,body{width:1200px;height:1037px;overflow:hidden;background:var(--board)}
body{font-family:"Roboto",Arial,sans-serif;color:var(--ink)}
.board{position:absolute;left:0;top:0;width:2072px;height:1791px;transform:scale(.5792);transform-origin:0 0}
.wires{position:absolute;left:0;top:0}
.screen-title{position:absolute;font-size:50px;font-weight:400;color:var(--title);white-space:nowrap;transform:translateX(-50%)}
.screen{position:absolute;width:244px;height:532px;background:var(--screen);border-radius:26px;overflow:hidden;box-shadow:0 12px 34px rgba(0,0,0,.10)}
.abs{position:absolute}
.bar-teal{position:absolute;left:0;top:0;width:100%;background:var(--teal)}
.hdr-title{position:absolute;left:0;right:0;text-align:center;font-size:10px;color:var(--white)}
.hdr-title.dark{color:var(--ink)}
.hdr-icons{position:absolute;right:18px;display:flex;gap:8px}
.hdr-icons i{display:block;width:6px;height:7px;background:var(--white)}
.hdr-icons i.funnel{clip-path:polygon(0 0,100% 0,62% 50%,62% 100%,38% 100%,38% 50%)}
.hdr-icons i.user{clip-path:circle(50% at 50% 50%);height:6px;width:6px}
.hdr-icons.dark i{background:var(--ink)}
.menu{position:absolute;left:18px;width:10px;height:8px;border-top:1.5px solid var(--white);border-bottom:1.5px solid var(--white)}
.menu::after{content:"";position:absolute;left:0;right:0;top:2px;border-top:1.5px solid var(--white)}
.search{position:absolute;left:18px;right:18px;height:21px;border-radius:11px;background:var(--white);font-size:5.5px;color:#b8bcc2;padding:7px 12px;box-shadow:0 1px 4px rgba(0,0,0,.06)}
.search::after{content:"";position:absolute;right:10px;top:6px;width:6px;height:6px;border:1px solid #b8bcc2;border-radius:50%}
.sec-head{position:absolute;left:18px;right:18px;display:flex;justify-content:space-between;align-items:baseline}
.sec-head h3{font-size:9px;font-weight:500}
.sec-head span{font-size:4.5px;color:var(--pink)}
.card{position:absolute;background:var(--white);border-radius:4px;overflow:hidden;box-shadow:0 1px 5px rgba(0,0,0,.07)}
.photo{position:relative;background:linear-gradient(160deg,var(--photo-a) 0%,var(--photo-b) 55%,var(--photo-c) 80%,var(--photo-a) 100%);color:var(--white)}
.tag{position:absolute;left:0;top:10px;background:var(--teal);color:var(--white);font-size:4.5px;padding:2px 8px}
.tag.pink{background:var(--pink)}
.countdown{position:absolute;left:0;right:0;text-align:center;font-weight:700;letter-spacing:.5px}
.units{display:flex;justify-content:center;gap:22px;font-size:3.5px;font-weight:400;opacity:.85;letter-spacing:0}
.cap{position:absolute;left:10px;bottom:8px;line-height:1.15}
.cap small{display:block;font-size:3.6px;opacity:.9}
.cap small.teal{color:var(--teal)}
.cap strong{display:block;font-weight:400}
.meta{display:grid;grid-template-columns:1fr 1fr;gap:5px 6px;padding:7px 10px;font-size:4.2px;color:var(--ink)}
.meta span::before{content:"";display:inline-block;width:3.5px;height:3.5px;border-radius:1px;background:var(--ink);margin-right:3px;vertical-align:middle}
.actions{display:flex;justify-content:space-around;padding:4px 10px 6px;border-top:1px solid var(--line)}
.pill{display:inline-block;border-radius:6px;font-size:4px;color:var(--white);padding:2.5px 12px;text-align:center}
.pill.pink{background:var(--pink)}
.pill.teal{background:var(--teal)}
.cta{position:absolute;left:18px;right:18px;height:23px;border-radius:12px;background:var(--teal);color:var(--white);font-size:7px;text-align:center;line-height:23px;letter-spacing:.3px}
.dropdown{position:absolute;left:28px;top:48px;background:var(--white);border-radius:2px;font-size:5px;line-height:15px;padding:0 4px;color:var(--teal);box-shadow:0 1px 4px rgba(0,0,0,.1)}
.dropdown span{display:block}
.dropdown span+span{color:#b8bcc2}
.od-hero{position:absolute;left:0;top:0;width:100%;height:190px}
.od-body{position:absolute;left:0;top:182px;width:100%;height:350px;background:var(--white);border-radius:8px 8px 0 0}
.od-body .row{position:absolute;left:18px;right:18px;font-size:5.2px;line-height:1.25}
.row .dot{display:inline-block;width:4px;height:4px;border-radius:1px;background:var(--ink);margin-right:5px;vertical-align:middle}
.btn{position:absolute;height:18px;color:var(--white);font-size:6px;text-align:center;line-height:18px}
.tabs{position:absolute;left:0;right:0;top:352px;height:24px;background:#f2f4f6;display:flex;font-size:6px}
.tabs span{flex:1;text-align:center;line-height:24px}
.tabs span:first-child{color:var(--teal);border-bottom:1.5px solid var(--teal)}
.lorem{font-size:3.6px;color:var(--muted);line-height:1.5}
.map{background:var(--map)}
.footer-bar{position:absolute;left:18px;right:18px;display:flex;gap:4px;font-size:6px}
.footer-bar span{flex:1;background:#eef0f2;text-align:center;line-height:17px;color:var(--muted)}
.footer-bar span.buy{flex:2;background:var(--yellow);color:var(--ink)}
.avatar{position:absolute;width:22px;height:22px;border-radius:50%;background:linear-gradient(135deg,#d9b8a4,#a07a66);border:1.5px solid var(--white)}
.avatar.alt{background:linear-gradient(135deg,#6b5a55,#2f2725)}
.msg-meta{position:absolute;font-size:3px;color:var(--muted)}
.bubble{position:absolute;font-size:5.5px;padding:5px 8px;background:#eceef0;color:var(--ink);border-radius:2px;white-space:nowrap}
.bubble.me{background:var(--teal);color:var(--white)}
.input-bar{position:absolute;left:18px;top:490px;width:178px;height:23px;border-radius:12px;border:1px solid #cfd3d8;background:var(--white)}
.mic{position:absolute;left:204px;top:490px;width:23px;height:23px;border-radius:50%;background:var(--teal)}
.mic::after{content:"";position:absolute;left:9px;top:6px;width:5px;height:9px;border-radius:3px;background:var(--white)}
.form-label{position:absolute;left:18px;font-size:5.5px;font-weight:500}
.field{position:absolute;height:20px;background:#eef0f3;border-radius:2px;font-size:5px;color:#a9adb3;line-height:20px;padding-left:22px;white-space:nowrap;overflow:hidden}
.field::before{content:"";position:absolute;left:9px;top:7px;width:5px;height:5px;border-radius:1px;background:var(--teal)}
.field.plain{padding-left:8px}
.field.plain::before{display:none}
.field.tall{height:40px;line-height:1.5;white-space:normal;padding:9px 8px;font-size:3.6px}
.back{position:absolute;left:18px;width:9px;height:1.5px;background:var(--white)}
.back::before{content:"";position:absolute;left:0;top:-2.5px;width:4px;height:4px;border-left:1.5px solid var(--white);border-bottom:1.5px solid var(--white);transform:rotate(45deg)}
</style>
</head>
<body>
<div class="board">

  <svg class="wires" width="2072" height="1791" viewBox="0 0 2072 1791" fill="none" stroke="#3a3a3a" stroke-width="1.5">
    <polyline points="410,751 607,751"/>
    <polyline points="703,655 607,655 607,1020 703,1020"/>
    <polyline points="945,514 1142,514"/>
    <polyline points="845,522 1089,522 1089,1605"/>
    <polyline points="1432,586 1630,586"/>
    <polyline points="208,905 99,905 99,1605 1795,1605 1795,826"/>
    <polyline points="306,1127 306,1561 1333,1561 1333,1495"/>
    <g fill="#111" stroke="none">
      <circle cx="410" cy="751" r="3.5"/><circle cx="945" cy="514" r="3.5"/>
      <circle cx="845" cy="522" r="3.5"/><circle cx="1432" cy="586" r="3.5"/>
      <circle cx="208" cy="905" r="3.5"/>
    </g>
  </svg>

  <h2 class="screen-title" style="left:862px;top:166px">Event List View</h2>
  <h2 class="screen-title" style="left:1319px;top:166px">Event Overview</h2>
  <h2 class="screen-title" style="left:1804px;top:166px">Group Chat Screen</h2>
  <h2 class="screen-title" style="left:296px;top:515px">Landing Page</h2>
  <h2 class="screen-title" style="left:866px;top:868px">Event Map View</h2>
  <h2 class="screen-title" style="left:1320px;top:874px">Create Event Form</h2>

  <!-- Landing page -->
  <section class="screen landing" style="left:182px;top:623px">
    <div class="bar-teal" style="height:108px"></div>
    <div class="hdr-title" style="top:47px">Landing Page</div>
    <div class="hdr-icons" style="top:49px"><i class="funnel"></i><i class="user"></i></div>
    <div class="search" style="top:75px">Search Events...</div>

    <div class="sec-head" style="top:122px"><h3>Latest Events</h3><span>See All</span></div>
    <article class="card" style="left:18px;top:140px;width:130px">
      <div class="photo" style="height:101px" role="img" aria-label="Concert crowd under purple stage lights">
        <span class="tag">Now</span>
        <div class="countdown" style="top:38px;font-size:15px">48 : 34 : 45<div class="units"><span>HOURS</span><span>MINUTES</span><span>SECONDS</span></div></div>
        <div class="cap" style="font-size:7px"><small>Ivo Marsh Start the Event</small><strong>Carnival Night Festival</strong><small>Organized by Rona Telfer</small></div>
      </div>
      <div class="meta" style="grid-template-columns:1fr;gap:4px;font-size:3.8px"><span>Tue, 10 Mar 2020 to Mon, 15 Mar 2020</span><span>08:00 PM - 11:30 PM</span></div>
      <div class="actions"><span class="pill pink">Stream Chat</span><span class="pill teal">Start Event</span></div>
    </article>
    <article class="card" style="left:156px;top:140px;width:130px">
      <div class="photo" style="height:101px" role="img" aria-label="Concert crowd under purple stage lights">
        <span class="tag pink">Soon</span>
        <div class="countdown" style="top:38px;font-size:15px">48 : 34 : 45<div class="units"><span>HOURS</span><span>MINUTES</span><span>SECONDS</span></div></div>
        <div class="cap" style="font-size:7px"><small>Ivo Marsh Start the Event</small><strong>Carnival Night Festival</strong><small>Organized by Rona Telfer</small></div>
      </div>
      <div class="meta" style="grid-template-columns:1fr;gap:4px;font-size:3.8px"><span>Tue, 10 Mar 2020 to Mon, 15 Mar 2020</span><span>08:00 PM - 11:30 PM</span></div>
      <div class="actions"><span class="pill pink">Stream Chat</span><span class="pill teal">Start Event</span></div>
    </article>

    <div class="sec-head" style="top:310px"><h3>Nearest Events</h3><span>See All</span></div>
    <article class="card" style="left:18px;top:327px;width:130px">
      <div class="photo" style="height:101px" role="img" aria-label="Concert crowd under purple stage lights">
        <span class="tag">Now</span>
        <div class="countdown" style="top:38px;font-size:15px">48 : 34 : 45<div class="units"><span>HOURS</span><span>MINUTES</span><span>SECONDS</span></div></div>
        <div class="cap" style="font-size:7px"><small>Ivo Marsh Start the Event</small><strong>Carnival Night Festival</strong><small>Organized by Rona Telfer</small></div>
      </div>
      <div class="meta" style="grid-template-columns:1fr;gap:4px;font-size:3.8px"><span>Tue, 10 Mar 2020 to Mon, 15 Mar 2020</span><span>08:00 PM - 11:30 PM</span></div>
      <div class="actions"><span class="pill pink">Stream Chat</span><span class="pill teal">Start Event</span></div>
    </article>
    <article class="card" style="left:156px;top:327px;width:130px">
      <div class="photo" style="height:101px" role="img" aria-label="Concert crowd under purple stage lights">
        <span class="tag pink">Soon</span>
        <div class="countdown" style="top:38px;font-size:15px">48 : 34 : 45<div class="units"><span>HOURS</span><span>MINUTES</span><span>SECONDS</span></div></div>
        <div class="cap" style="font-size:7px"><small>Ivo Marsh Start the Event</small><strong>Carnival Night Festival</strong><small>Organized by Rona Telfer</small></div>
      </div>
      <div class="meta" style="grid-template-columns:1fr;gap:4px;font-size:3.8px"><span>Tue, 10 Mar 2020 to Mon, 15 Mar 2020</span><span>08:00 PM - 11:30 PM</span></div>
      <div class="actions"><span class="pill pink">Stream Chat</span><span class="pill teal">Start Event</span></div>
    </article>

    <div class="cta" style="top:492px">CREATE NEW KELVO (EVENT)</div>
  </section>

  <!-- Event list view -->
  <section class="screen event-list" style="left:748px;top:243px">
    <div class="bar-teal" style="height:108px"></div>
    <div class="menu" style="top:50px"></div>
    <div class="dropdown"><span>List View</span><span>Map View</span></div>
    <div class="hdr-title" style="top:47px">Events List</div>
    <div class="hdr-icons" style="top:49px"><i class="funnel"></i><i class="user"></i></div>
    <div class="search" style="top:76px">Search Events...</div>

    <article class="card" style="left:18px;top:125px;width:207px">
      <div class="photo" style="height:110px" role="img" aria-label="Concert crowd under purple stage lights">
        <span class="tag">Now</span>
        <div class="countdown" style="top:32px;font-size:21px">48 : 34 : 45<div class="units" style="gap:30px"><span>HOURS</span><span>MINUTES</span><span>SECONDS</span></div></div>
        <div class="cap" style="font-size:8px"><small class="teal">Ivo Marsh Started Events</small><strong>Carnival Night Festival</strong><small>Organized by Rona Telfer</small></div>
      </div>
      <div class="meta" style="grid-template-columns:1.1fr 1fr .7fr"><span>Tue, 10 Mar 2020 to Mon,</span><span>08:00 PM - 11:30 PM</span><span>2.4 km</span><span>20 Friends</span><span>300 Peoples</span><span>12k Interested</span></div>
      <div class="actions"><span class="pill pink" style="padding:2.5px 18px">Event Feed</span><span class="pill teal" style="padding:2.5px 18px">Event Detail</span></div>
    </article>
    <article class="card" style="left:18px;top:301px;width:207px">
      <div class="photo" style="height:110px" role="img" aria-label="Concert crowd under purple stage lights">
        <span class="tag">Now</span>
        <div class="countdown" style="top:32px;font-size:21px">48 : 34 : 45<div class="units" style="gap:30px"><span>HOURS</span><span>MINUTES</span><span>SECONDS</span></div></div>
        <div class="cap" style="font-size:8px"><small class="teal">Ivo Marsh Started Events</small><strong>Carnival Night Festival</strong><small>Organized by Rona Telfer</small></div>
      </div>
      <div class="meta" style="grid-template-columns:1.1fr 1fr .7fr"><span>Tue, 10 Mar 2020 to Mon,</span><span>08:00 PM - 11:30 PM</span><span>2.4 km</span><span>20 Friends</span><span>300 Peoples</span><span>12k Interested</span></div>
      <div class="actions"><span class="pill pink" style="padding:2.5px 18px">Event Feed</span><span class="pill teal" style="padding:2.5px 18px">Event Detail</span></div>
    </article>
    <article class="card" style="left:18px;top:477px;width:207px">
      <div class="photo" style="height:110px" role="img" aria-label="Concert crowd under purple stage lights">
        <span class="tag">Now</span>
        <div class="countdown" style="top:32px;font-size:21px">48 : 34 : 45</div>
      </div>
    </article>
  </section>

  <!-- Event overview -->
  <section class="screen overview" style="left:1198px;top:254px">
    <div class="photo od-hero" role="img" aria-label="Festival crowd with raised hands under purple stage lights"></div>
    <div class="menu" style="top:50px"></div>
    <div class="hdr-title" style="top:47px">Event Details</div>
    <div class="hdr-icons" style="top:49px"><i class="funnel"></i><i class="user"></i></div>
    <div class="countdown abs" style="top:95px;font-size:31px;color:var(--white)">48 : 34 : 45<div class="units" style="font-size:5px;gap:36px"><span>HOURS</span><span>MINUTES</span><span>SECONDS</span></div></div>
    <div class="od-body">
      <span class="tag" style="left:auto;right:18px;top:4px;padding:4px 6px;font-size:6px">Now</span>
      <div class="row" style="top:13px;font-size:10px;font-weight:500">Carnival Night Festival</div>
      <div class="row" style="top:33px"><span class="dot" style="border-radius:50%;width:7px;height:7px;background:#a07a66"></span>Organized by <span style="color:var(--teal)">Rona Telfer</span></div>
      <div class="row" style="top:52px"><span class="dot"></span>Tue, 10 Mar 2020 to Mon, 15 Mar 2020</div>
      <div class="row" style="top:64px"><span class="dot"></span>08:00 PM - 11:30 PM</div>
      <div class="row" style="top:76px;padding-left:9px;text-indent:-9px"><span class="dot"></span>2.4 km, 12 Linden Row 1st Cross, Harrow Park, Westvale-40210</div>
      <div class="row" style="top:97px"><span class="dot"></span>300 Peoples</div>
      <div class="row" style="top:117px;display:flex;align-items:center;gap:6px;font-size:4px;color:var(--teal);border-bottom:1px solid var(--line);padding-bottom:6px">
        <span style="display:inline-flex"><i class="dot" style="width:8px;height:8px;border-radius:50%;background:#a07a66;margin:0 -2px 0 0"></i><i class="dot" style="width:8px;height:8px;border-radius:50%;background:#5c4b46;margin:0 -2px 0 0"></i><i class="dot" style="width:8px;height:8px;border-radius:50%;background:#c9a08c"></i></span>12k Interested
        <span style="margin-left:auto;color:var(--pink);padding-right:22px">12k Views</span>
      </div>
      <div class="btn" style="left:18px;top:142px;width:98px;background:var(--teal)">Get Directions</div>
      <div class="btn" style="left:127px;top:142px;width:98px;background:var(--pink)">Send Message</div>
      <div class="tabs" style="top:170px"><span>Events Details</span><span>Offers</span></div>
      <div class="row" style="top:203px;font-size:5px;font-weight:500">About The Event</div>
      <p class="row lorem" style="top:212px">Plain sample copy that shows where the event story goes, with a short look at the lineup, the stage, food stalls, entry rules and what guests can expect on the night once gates open.</p>
      <div class="map abs" role="img" aria-label="Street map around the venue" style="left:0;top:245px;width:100%;height:64px"></div>
    </div>
    <div class="footer-bar" style="top:500px"><span>Like</span><span>Invite</span><span class="buy">Buy Ticket</span></div>
  </section>

  <!-- Group chat -->
  <section class="screen chat" style="left:1686px;top:254px">
    <div class="bar-teal" style="height:72px"></div>
    <div class="back" style="top:54px"></div>
    <div class="avatar" role="img" aria-label="Profile photo of Tessa" style="left:38px;top:43px"></div>
    <div class="abs" style="left:66px;top:45px;font-size:6px;color:var(--white);line-height:1.3">Tessa<br><span style="font-size:4.5px;opacity:.85">● Online</span></div>
    <div class="hdr-icons" style="top:51px;gap:10px"><i style="width:8px;height:5px;border-radius:1px"></i><i style="width:6px;height:6px;border-radius:2px"></i><i style="width:2px;height:7px"></i></div>

    <div class="avatar" role="img" aria-label="Profile photo of Mira" style="left:18px;top:95px"></div>
    <div class="msg-meta" style="left:50px;top:97px">Mira, 9:50 PM</div>
    <div class="bubble" style="left:50px;top:104px">Hello.</div>
    <div class="bubble" style="left:50px;top:124px">How are you?</div>

    <div class="msg-meta" style="left:180px;top:151px">9:52 PM</div>
    <div class="bubble me" style="right:50px;top:157px">I am fine, how are you Mira?</div>
    <div class="avatar" role="img" aria-label="Profile photo of Tessa" style="left:204px;top:150px"></div>

    <div class="avatar alt" role="img" aria-label="Profile photo of Rona Telfer" style="left:18px;top:185px"></div>
    <div class="msg-meta" style="left:50px;top:188px">Rona Telfer, 9:53 PM</div>
    <div class="bubble" style="left:50px;top:195px">Hello.</div>

    <div class="msg-meta" style="left:180px;top:219px">9:54 PM</div>
    <div class="bubble me" style="right:50px;top:226px">Hello Rona, How are you?</div>
    <div class="avatar" role="img" aria-label="Profile photo of Tessa" style="left:204px;top:219px"></div>

    <div class="avatar" role="img" aria-label="Profile photo of Mira" style="left:18px;top:254px"></div>
    <div class="msg-meta" style="left:50px;top:256px">Mira, 9:57 PM</div>
    <div class="photo abs" role="img" aria-label="Shared photo of a concert crowd under purple lights" style="left:50px;top:263px;width:140px;height:94px;border:2px solid var(--white)"></div>

    <div class="msg-meta" style="left:186px;top:368px">10:00 PM</div>
    <div class="bubble me" style="right:50px;top:374px">Yes.</div>
    <div class="avatar" role="img" aria-label="Profile photo of Tessa" style="left:204px;top:367px"></div>

    <div class="avatar alt" role="img" aria-label="Profile photo of Rona Telfer" style="left:18px;top:403px"></div>
    <div class="msg-meta" style="left:50px;top:405px">Rona Telfer, 10:01 PM</div>
    <div class="bubble" style="left:50px;top:412px">Yes.</div>

    <div class="avatar" role="img" aria-label="Profile photo of Mira" style="left:18px;top:443px"></div>
    <div class="msg-meta" style="left:50px;top:445px">Mira, 10:02 PM</div>
    <div class="bubble" style="left:50px;top:452px">Good.</div>

    <div class="input-bar"></div>
    <div class="mic"></div>
  </section>

  <!-- Event map view -->
  <section class="screen map-view" style="left:762px;top:950px">
    <div class="abs" style="left:18px;top:49px;width:10px;height:8px;border-top:1.5px solid var(--ink);border-bottom:1.5px solid var(--ink)"></div>
    <div class="hdr-title dark" style="top:47px">Events Map View</div>
    <div class="hdr-icons dark" style="top:49px"><i class="funnel"></i><i class="user"></i></div>
    <div class="map abs" role="img" aria-label="Street map of the city with nearby event locations" style="left:0;top:95px;width:100%;height:437px"></div>
    <div class="search" style="top:76px">Search Events...</div>
    <article class="card" style="left:18px;top:372px;width:140px;height:113px">
      <div class="photo" style="height:80px" role="img" aria-label="Concert crowd under purple stage lights">
        <div class="cap" style="font-size:7.5px"><strong>Carnival Night Festival</strong></div>
      </div>
      <div class="meta" style="grid-template-columns:1fr;gap:4px"><span>Tue, 10 Mar 2020</span><span>08:00 PM</span></div>
    </article>
    <article class="card" style="left:168px;top:372px;width:140px;height:113px">
      <div class="photo" style="height:80px" role="img" aria-label="Concert crowd under purple stage lights">
        <div class="cap" style="font-size:7.5px"><strong>Carnival Night Festival</strong></div>
      </div>
      <div class="meta" style="grid-template-columns:1fr;gap:4px"><span>Tue, 10 Mar 2020</span><span>08:00 PM</span></div>
    </article>
  </section>

  <!-- Create event form -->
  <section class="screen create-form" style="left:1224px;top:950px">
    <div class="bar-teal" style="height:72px"></div>
    <div class="back" style="top:54px"></div>
    <div class="hdr-title" style="top:48px">Create New Kelvo</div>

    <div class="form-label" style="top:88px">Place:</div>
    <div class="field" style="left:18px;top:101px;width:207px">12 Linden Row 1st Cross, Harrow Park, Westvale</div>
    <div class="form-label" style="top:134px">Time Start:</div>
    <div class="form-label" style="top:134px;left:132px">Time End:</div>
    <div class="field" style="left:18px;top:147px;width:92px">10:30 PM - 27/02/2020</div>
    <div class="field" style="left:133px;top:147px;width:92px">10:30 PM - 29/02/2020</div>
    <div class="form-label" style="top:180px">Tags:</div>
    <div class="field" style="left:18px;top:193px;width:207px">#drink, #bar, #happyhour</div>
    <div class="form-label" style="top:226px">Category:</div>
    <div class="field" style="left:18px;top:239px;width:207px">Select Category<span style="position:absolute;right:10px;color:var(--muted)">▾</span></div>
    <div class="form-label" style="top:272px">Members Invites:</div>
    <div class="field" style="left:18px;top:285px;width:207px">Invites</div>
    <div class="form-label" style="top:318px">Description:</div>
    <div class="field plain tall" style="left:18px;top:331px;width:207px">Sample note that marks where the host adds a short summary of the event, the timing, the dress code and any entry details guests should read first.</div>
    <div class="form-label" style="top:380px">Images:</div>
    <div class="field" style="left:18px;top:393px;width:207px">Image 1, Image 2</div>
    <div class="abs" style="left:18px;top:430px;font-size:9px;font-weight:500">Offers:</div>
    <div class="form-label" style="top:456px">Title:</div>
    <div class="form-label" style="top:456px;left:132px">Images:</div>
    <div class="field plain" style="left:18px;top:468px;width:92px">Linden Row</div>
    <div class="field plain" style="left:133px;top:468px;width:92px">Image 1</div>
    <div class="form-label" style="top:502px">Link:</div>
    <div class="field plain" style="left:18px;top:514px;width:207px"></div>
  </section>

</div>
</body>
</html>
```